Powerpoint design template for PLAYNOVA for new digital platform

We would like to use a PowerPoint template, we would like to create a new page, we would like to create a new digital platform PLAYNOVA for schools and parents for the creation of playful communication and educational tools for children to enhance their positive development, amaze them learn in a playful way. This platform is going to be the most creative, stimulating and innovative classroom, easy to use and fast to implement. Scrapbooking, collages ... Magazine, newsletters Diplomla / awards Slideshows Facebook Calendars Organizers Greetings Games ... This powerpoint template will be used essential to We are looking for a professional design, positioning our brand in the children market with an adult hearing. so you will need to find a good deal. Primary target: nurseries & schools from 0 to 18 years old and universities (in 2nd phase) Secondary target: small & medium businesses Third target: general public, and TPE If it is a color scheme, then it is suggested that it be marketed in Europe (UK, Italy, Spain) and in a 2nd Stage USA and other countries. multiple options for front page, insidious pages (multiple styles with limited text and extended text) and final contact page We need something to read, we can not do it too much, but we can not do it. , and inside pages aligned to our logo

Target Market(s)

Target 1; Education with teacher Target 2; parents and grandparents

Industry/Entity Type

Education

Font styles to use
Other font styles liked:
• not decided. but not too fancy

Requirements
Must have
• Multi page options for front page, page insides (multiple styles with limited text and extended text) and final page contact
Nice to have
• do not have a lot of ideas. We need something to read, we can not get away from it
Should not have
• not too fancy and busy: keep clarity & simplicity while reassuring on quality

```html
<!DOCTYPE html>
<html lang="en">
<head>
<meta charset="utf-8">
<title>PLAYNOVA presentation template</title>
<link href="https://fonts.googleapis.com/css2?family=Baloo+2:wght@700;800&family=Open+Sans:wght@400;600&display=swap" rel="stylesheet">
<style>
:root{
  --page:#e9e9e9;
  --lime:#c3d92b;
  --lime-dark:#8fbc2a;
  --blue:#3aa8ea;
  --ink:#4a4a4a;
  --ink-dark:#262626;
  --white:#ffffff;
}
*{box-sizing:border-box;margin:0;padding:0}
html,body{width:1200px;height:1200px;overflow:hidden;background:var(--page)}
body{position:relative;font-family:"Open Sans",Arial,sans-serif;color:var(--ink)}
.slide{position:absolute;width:381px;height:214px;background:var(--white);overflow:hidden;box-shadow:0 1px 3px rgba(0,0,0,.25)}
.c1{left:14px}.c2{left:410px}.c3{left:808px}
.r1{top:43px}.r2{top:322px}.r3{top:600px}.r4{top:878px}
.abs{position:absolute}

/* cover */
.cover-photo{position:absolute;inset:0}
.cover-photo::after{content:"";position:absolute;inset:0;background:rgba(255,255,255,.45)}
.cover-band-back{position:absolute;inset:0;background:var(--lime-dark);clip-path:polygon(0 106px,378px 112px,376px 200px,0 196px)}
.cover-band{position:absolute;inset:0;background:var(--lime);clip-path:polygon(0 112px,370px 118px,366px 190px,0 188px)}
.cover-logo{position:absolute;left:98px;top:58px;width:262px;text-align:center;font-family:"Baloo 2",sans-serif;font-weight:800;font-size:50px;line-height:1;color:var(--ink-dark);letter-spacing:1px}
.cover-headline{position:absolute;left:22px;top:131px;font-family:"Baloo 2",sans-serif;font-weight:700;font-size:20px;color:var(--white);text-shadow:1px 1px 1px rgba(0,0,0,.45);line-height:1}
.cover-sub{position:absolute;left:22px;top:157px;font-size:8px;color:var(--white);text-shadow:1px 1px 1px rgba(0,0,0,.4)}
.cover-tagline{position:absolute;left:13px;top:193px;font-size:6.5px;color:var(--ink-dark);font-style:italic}

/* inner header */
.band-back{position:absolute;inset:0;background:var(--lime-dark);clip-path:polygon(0 0,381px 0,376px 50px,0 50px)}
.band{position:absolute;inset:0;background:var(--lime);clip-path:polygon(0 0,372px 0,372px 44px,0 48px)}
.headline{position:absolute;left:30px;top:21px;font-family:"Baloo 2",sans-serif;font-weight:700;font-size:12px;color:var(--white);text-shadow:1px 1px 1px rgba(0,0,0,.45);line-height:1.2}
.brand{position:absolute;right:24px;top:13px;font-family:"Baloo 2",sans-serif;font-weight:800;font-size:15px;line-height:1;color:var(--ink-dark)}
.footer{position:absolute;left:29px;right:29px;bottom:4px;display:flex;justify-content:space-between;font-size:4.5px;color:var(--lime-dark);font-weight:600}

.txt{font-size:5px;line-height:1.45;color:var(--ink)}
.photo{position:absolute}
.frame{position:absolute;background:var(--blue)}
.vtitle{position:absolute;font-size:6px;color:var(--blue);letter-spacing:1px;transform:rotate(-90deg);transform-origin:left top;font-weight:600}
ul.bullets{list-style:none}
ul.bullets li{position:relative;padding-left:8px;margin-bottom:6px}
ul.bullets li::before{content:"";position:absolute;left:1px;top:2.5px;width:2.5px;height:2.5px;background:var(--blue)}
.col-title{font-size:8px;color:var(--blue);margin-bottom:6px}

.card-back{position:absolute;background:var(--blue);transform:rotate(2deg)}
.card{position:absolute;background:var(--white);box-shadow:0 0 2px rgba(0,0,0,.3);padding:12px 8px 8px 8px;transform:rotate(-1deg)}
.card ul.bullets li{font-size:6px;line-height:1.4;margin-bottom:8px}

.step-row{position:absolute;left:32px;top:74px;display:flex;gap:2px}
.step{width:66px;height:32px;background:var(--blue);clip-path:polygon(0 0,56px 0,66px 16px,56px 32px,0 32px,10px 16px);display:flex;align-items:center;justify-content:center;color:var(--white);font-size:6.5px;letter-spacing:1px;font-weight:600}
.step-texts{position:absolute;left:35px;top:112px;display:flex;gap:6px}
.step-texts p{width:56px;font-size:4.3px;line-height:1.45}

.box-label{position:absolute;left:36px;width:80px;height:34px;border:1px solid var(--blue);box-shadow:-2px 2px 0 var(--blue);font-size:5px;line-height:1.4;text-align:center;padding-top:5px;background:var(--white)}

.chart-title{font-size:8px;color:var(--blue);letter-spacing:1px;font-weight:600}
.chart-sub{font-size:5.5px}

table.data{position:absolute;left:16px;top:60px;width:172px;border-collapse:collapse;font-size:5.5px}
table.data td{height:18px;border-bottom:1.2px solid var(--blue);text-align:right;padding-right:4px}
table.data td:first-child{text-align:left;padding-left:4px}
table.data tr:first-child td:not(:first-child){color:var(--blue)}
table.data tr:last-child td{font-weight:600;border-bottom:none}
</style>
</head>
<body>

<!-- Row 1: covers -->
<section class="slide c1 r1">
  <div class="cover-band-back"></div><div class="cover-band"></div>
  <div class="cover-logo">PLAYNOVA</div>
  <div class="cover-headline">Headline</div>
  <div class="cover-sub">Lorem ipsum dolor sit amet, consetetur sadipscing</div>
  <div class="cover-tagline">YOUR TAGLINE GOES HERE</div>
</section>

<section class="slide c2 r1">
  <div class="cover-photo" role="img" aria-label="Photo of schoolchildren with backpacks walking towards a school building" style="background:linear-gradient(180deg,#b9a48f 0%,#c9b9a6 45%,#8ea3b8 75%,#6e7f96 100%)"></div>
  <div class="cover-band-back"></div><div class="cover-band"></div>
  <div class="cover-logo">PLAYNOVA</div>
  <div class="cover-headline">Headline</div>
  <div class="cover-sub">Lorem ipsum dolor sit amet, consetetur sadipscing</div>
  <div class="cover-tagline">YOUR TAGLINE GOES HERE</div>
</section>

<section class="slide c3 r1">
  <div class="cover-photo" role="img" aria-label="Photo of a girl drawing at a desk with coloured pencils" style="background:linear-gradient(135deg,#e7c7b0 0%,#d89aa6 40%,#e8d6c8 70%,#9ec07a 100%)"></div>
  <div class="cover-band-back"></div><div class="cover-band"></div>
  <div class="cover-logo">PLAYNOVA</div>
  <div class="cover-headline">Headline</div>
  <div class="cover-sub">Lorem ipsum dolor sit amet, consetetur sadipscing</div>
  <div class="cover-tagline">YOUR TAGLINE GOES HERE</div>
</section>

<!-- Row 2 -->
<section class="slide c1 r2">
  <div class="band-back"></div><div class="band"></div>
  <div class="headline">Headline</div><div class="brand">PLAYNOVA</div>
  <div class="vtitle" style="left:40px;top:92px">TITLE</div>
  <div class="vtitle" style="left:40px;top:144px">TITLE</div>
  <div class="vtitle" style="left:40px;top:196px">TITLE</div>
  <div class="frame" style="left:49px;top:53px;width:122px;height:45px"></div>
  <div class="photo" role="img" aria-label="Photo of children writing at school desks" style="left:46px;top:50px;width:122px;height:44px;background:linear-gradient(90deg,#c8b8a4,#8fa9c3)"></div>
  <div class="frame" style="left:49px;top:105px;width:122px;height:45px"></div>
  <div class="photo" role="img" aria-label="Photo of a girl drawing with pencils" style="left:46px;top:102px;width:122px;height:44px;background:linear-gradient(90deg,#e3b5a9,#d96c8a,#e9c85e)"></div>
  <div class="frame" style="left:49px;top:157px;width:122px;height:45px"></div>
  <div class="photo" role="img" aria-label="Photo of smiling children in a classroom" style="left:46px;top:154px;width:122px;height:44px;background:linear-gradient(90deg,#e07a5a,#f1c27d,#7fb5d8)"></div>
  <p class="txt abs" style="left:174px;top:57px;width:176px">Lorem ipsum dolor sit amet, consetetur sadipscing elitr, sed diam nonumy eirmod tempor invidunt ut labore et dolore magna aliquyam erat, sed diam voluptua. At vero eos et accusam et justo duo dolores et ea rebum.</p>
  <p class="txt abs" style="left:174px;top:109px;width:176px">Lorem ipsum dolor sit amet, consetetur sadipscing elitr, sed diam nonumy eirmod tempor invidunt ut labore et dolore magna aliquyam erat, sed diam voluptua. At vero eos et accusam et justo duo dolores et ea rebum.</p>
  <p class="txt abs" style="left:174px;top:161px;width:176px">Lorem ipsum dolor sit amet, consetetur sadipscing elitr, sed diam nonumy eirmod tempor invidunt ut labore et dolore magna aliquyam erat, sed diam voluptua. At vero eos et accusam et justo duo dolores et ea rebum.</p>
  <div class="footer"><span>13.11.16</span><span>FOOTER</span><span>4</span></div>
</section>

<section class="slide c2 r2">
  <div class="band-back"></div><div class="band"></div>
  <div class="headline">Headline</div><div class="brand">PLAYNOVA</div>
  <div class="frame" style="left:18px;top:52px;width:340px;height:146px"></div>
  <div class="abs" style="left:24px;top:49px;width:330px;height:146px;background:var(--white)"></div>
  <div class="photo" role="img" aria-label="Photo of children writing at school desks" style="left:26px;top:52px;width:102px;height:44px;background:linear-gradient(90deg,#c8b8a4,#8fa9c3)"></div>
  <p class="txt abs" style="left:132px;top:56px;width:118px;text-align:center">Lorem ipsum dolor sit amet, consetetur sadipscing elitr, sed diam nonumy eirmod tempor invidunt ut labore et dolore magna aliquyam erat, sed diam voluptua.</p>
  <div class="photo" role="img" aria-label="Photo of smiling children in a classroom" style="left:254px;top:52px;width:101px;height:44px;background:linear-gradient(90deg,#e07a5a,#f1c27d,#7fb5d8)"></div>
  <div class="photo" role="img" aria-label="Photo of schoolchildren walking with backpacks" style="left:26px;top:100px;width:102px;height:44px;background:linear-gradient(90deg,#b9a48f,#8ea3b8)"></div>
  <p class="txt abs" style="left:132px;top:104px;width:118px;text-align:center">Lorem ipsum dolor sit amet, consetetur sadipscing elitr, sed diam nonumy eirmod tempor invidunt ut labore et dolore magna aliquyam erat, sed diam voluptua.</p>
  <div class="photo" role="img" aria-label="Photo of colourful school supplies" style="left:254px;top:100px;width:101px;height:44px;background:linear-gradient(90deg,#d94a4a,#f2b53a,#3f8fd1,#5cb85c)"></div>
  <div class="photo" role="img" aria-label="Photo of a girl drawing with pencils" style="left:26px;top:148px;width:102px;height:44px;background:linear-gradient(90deg,#e3b5a9,#d96c8a,#e9c85e)"></div>
  <p class="txt abs" style="left:132px;top:152px;width:118px;text-align:center">Lorem ipsum dolor sit amet, consetetur sadipscing elitr, sed diam nonumy eirmod tempor invidunt ut labore et dolore magna aliquyam erat, sed diam voluptua.</p>
  <div class="photo" role="img" aria-label="Photo of pink notebooks and stationery" style="left:254px;top:148px;width:101px;height:44px;background:linear-gradient(90deg,#e0457b,#f29bb5,#6f6f6f)"></div>
  <div class="footer"><span>13.11.16</span><span>FOOTER</span><span>5</span></div>
</section>

<section class="slide c3 r2">
  <div class="band-back"></div><div class="band"></div>
  <div class="headline">Headline</div><div class="brand">PLAYNOVA</div>
  <div class="frame" style="left:14px;top:62px;width:192px;height:140px;transform:rotate(-2deg)"></div>
  <div class="photo" role="img" aria-label="Photo of schoolchildren with backpacks walking towards a school entrance" style="left:22px;top:58px;width:190px;height:140px;background:linear-gradient(180deg,#c2ae96 0%,#a79580 50%,#7f93ab 80%,#5f6d80 100%)"></div>
  <ul class="bullets txt abs" style="left:224px;top:74px;width:146px;font-size:5.5px">
    <li>Lorem ipsum dolor sit amet, consetetur sadipscing elitr, sed diam nonumy eirmod</li>
    <li>Lorem ipsum dolor sit amet, consetetur sadipscing elitr, sed diam nonumy eirmod</li>
    <li>Lorem ipsum dolor sit amet, consetetur sadipscing elitr, sed diam nonumy eirmod</li>
    <li>Lorem ipsum dolor sit amet, consetetur sadipscing elitr, sed diam nonumy eirmod</li>
    <li>Lorem ipsum dolor sit amet, consetetur sadipscing elitr, sed diam nonumy eirmod</li>
  </ul>
  <div class="footer"><span>13.11.16</span><span>FOOTER</span><span>6</span></div>
</section>

<!-- Row 3 -->
<section class="slide c1 r3">
  <div class="band-back"></div><div class="band"></div>
  <div class="headline" style="top:23px">Headline</div><div class="brand">PLAYNOVA</div>
  <div class="frame" style="left:24px;top:56px;width:334px;height:142px;transform:rotate(-1deg)"></div>
  <div class="abs" style="left:28px;top:52px;width:324px;height:140px;background:var(--white);box-shadow:0 0 2px rgba(0,0,0,.3)"></div>
  <div class="abs txt" style="left:38px;top:58px;width:150px">
    <div class="col-title">Title</div>
    <ul class="bullets">
      <li>Lorem ipsum dolor sit amet, consetetur sadipscing elitr, sed diam nonumy eirmod tempor invidunt ut labore et dolore magna aliquyam erat, sed diam voluptua.</li>
      <li>Lorem ipsum dolor sit amet, consetetur sadipscing elitr, sed diam nonumy eirmod tempor invidunt ut labore et dolore magna aliquyam erat, sed diam voluptua.</li>
      <li>Lorem ipsum dolor sit amet, consetetur sadipscing elitr, sed diam nonumy eirmod tempor invidunt ut labore et dolore magna aliquyam erat, sed diam voluptua.</li>
    </ul>
  </div>
  <div class="abs txt" style="left:198px;top:58px;width:150px">
    <div class="col-title">Title</div>
    <ul class="bullets">
      <li>Lorem ipsum dolor sit amet, consetetur sadipscing elitr, sed diam nonumy eirmod tempor invidunt ut labore et dolore magna aliquyam erat, sed diam voluptua.</li>
      <li>Lorem ipsum dolor sit amet, consetetur sadipscing elitr, sed diam nonumy eirmod tempor invidunt ut labore et dolore magna aliquyam erat, sed diam voluptua.</li>
      <li>Lorem ipsum dolor sit amet, consetetur sadipscing elitr, sed diam nonumy eirmod tempor invidunt ut labore et dolore magna aliquyam erat, sed diam voluptua.</li>
    </ul>
  </div>
  <div class="footer"><span>13.11.16</span><span>FOOTER</span><span>7</span></div>
</section>

<section class="slide c2 r3">
  <div class="band-back"></div><div class="band"></div>
  <div class="headline" style="top:23px">Headline</div><div class="brand">PLAYNOVA</div>
  <div class="vtitle" style="left:26px;top:78px">Title</div>
  <div class="vtitle" style="left:26px;top:116px">Title</div>
  <div class="vtitle" style="left:26px;top:154px">Title</div>
  <div class="vtitle" style="left:26px;top:192px">Title</div>
  <div class="box-label" style="top:50px">Lorem ipsum dolor sit amet, consetetur sadipscing elitr</div>
  <div class="box-label" style="top:88px">Lorem ipsum dolor sit amet, consetetur sadipscing elitr</div>
  <div class="box-label" style="top:126px">Lorem ipsum dolor sit amet, consetetur sadipscing elitr</div>
  <div class="box-label" style="top:164px">Lorem ipsum dolor sit amet, consetetur sadipscing elitr</div>
  <p class="txt abs" style="left:122px;top:54px;width:205px">Lorem ipsum dolor sit amet, consetetur sadipscing elitr, sed diam nonumy eirmod tempor invidunt ut labore et dolore magna aliquyam erat, sed diam voluptua. At vero eos et accusam et justo duo dolores et ea rebum.</p>
  <p class="txt abs" style="left:122px;top:92px;width:205px">Lorem ipsum dolor sit amet, consetetur sadipscing elitr, sed diam nonumy eirmod tempor invidunt ut labore et dolore magna aliquyam erat, sed diam voluptua. At vero eos et accusam et justo duo dolores et ea rebum.</p>
  <p class="txt abs" style="left:122px;top:130px;width:205px">Lorem ipsum dolor sit amet, consetetur sadipscing elitr, sed diam nonumy eirmod tempor invidunt ut labore et dolore magna aliquyam erat, sed diam voluptua. At vero eos et accusam et justo duo dolores et ea rebum.</p>
  <p class="txt abs" style="left:122px;top:168px;width:205px">Lorem ipsum dolor sit amet, consetetur sadipscing elitr, sed diam nonumy eirmod tempor invidunt ut labore et dolore magna aliquyam erat, sed diam voluptua. At vero eos et accusam et justo duo dolores et ea rebum.</p>
  <div class="footer"><span>13.11.16</span><span>FOOTER</span><span>8</span></div>
</section>

<section class="slide c3 r3">
  <div class="band-back"></div><div class="band"></div>
  <div class="headline" style="top:23px">Headline</div><div class="brand">PLAYNOVA</div>
  <div class="step-row">
    <div class="step">TITLE</div><div class="step">TITLE</div><div class="step">TITLE</div><div class="step">TITLE</div><div class="step">TITLE</div>
  </div>
  <div class="step-texts">
    <p>Lorem ipsum dolor sit amet, consetetur sadipscing elitr, sed diam nonumy eirmod tempor invidunt ut labore et dolore magna aliquyam erat, sed diam voluptua. At vero eos et accusam</p>
    <p>Lorem ipsum dolor sit amet, consetetur sadipscing elitr, sed diam nonumy eirmod tempor invidunt ut labore et dolore magna aliquyam erat, sed diam voluptua. At vero eos et accusam</p>
    <p>Lorem ipsum dolor sit amet, consetetur sadipscing elitr, sed diam nonumy eirmod tempor invidunt ut labore et dolore magna aliquyam erat, sed diam voluptua. At vero eos et accusam</p>
    <p>Lorem ipsum dolor sit amet, consetetur sadipscing elitr, sed diam nonumy eirmod tempor invidunt ut labore et dolore magna aliquyam erat, sed diam voluptua. At vero eos et accusam</p>
    <p>Lorem ipsum dolor sit amet, consetetur sadipscing elitr, sed diam nonumy eirmod tempor invidunt ut labore et dolore magna aliquyam erat, sed diam voluptua. At vero eos et accusam</p>
  </div>
  <div class="footer"><span>13.11.16</span><span>FOOTER</span><span>9</span></div>
</section>

<!-- Row 4 -->
<section class="slide c1 r4">
  <div class="band-back"></div><div class="band"></div>
  <div class="headline" style="top:23px">Headline</div><div class="brand">PLAYNOVA</div>
  <div class="abs" style="left:32px;top:59px"><div class="chart-title">Title</div><div class="chart-sub">Text</div></div>
  <svg class="abs" style="left:30px;top:98px" width="176" height="90" viewBox="0 0 176 90" font-family="Open Sans, sans-serif" font-size="5.5" fill="#4a4a4a">
    <line x1="4" y1="73" x2="176" y2="73" stroke="#bbb" stroke-width=".6"/>
    <g fill="#3aa8ea">
      <rect x="10" y="56.5" width="12" height="16.5"/><rect x="30" y="47.8" width="12" height="25.2"/>
      <rect x="50" y="21.6" width="12" height="51.4"/><rect x="70" y="9" width="12" height="64"/>
      <rect x="90" y="29.4" width="12" height="43.6"/><rect x="110" y="40" width="12" height="33"/>
      <rect x="130" y="28.4" width="12" height="44.6"/><rect x="150" y="26.5" width="12" height="46.5"/>
    </g>
    <g text-anchor="middle">
      <text x="16" y="54">17</text><text x="36" y="45">26</text><text x="56" y="19">53</text><text x="76" y="6.5">66</text>
      <text x="96" y="27">45</text><text x="116" y="37.5">34</text><text x="136" y="26">46</text><text x="156" y="24">48</text>
      <text x="16" y="83">Text</text><text x="36" y="83">Text</text><text x="56" y="83">Text</text><text x="76" y="83">Text</text>
      <text x="96" y="83">Text</text><text x="116" y="83">Text</text><text x="136" y="83">Text</text><text x="156" y="83">Text</text>
    </g>
  </svg>
  <div class="card-back" style="left:222px;top:60px;width:132px;height:130px"></div>
  <div class="card" style="left:218px;top:62px;width:128px;height:122px">
    <ul class="bullets">
      <li>Lorem ipsum dolor sit amet, consetetur sadipscing elitr, sed diam nonumy eirmod tempor invidunt ut labore et dolore</li>
      <li>Lorem ipsum dolor sit amet, consetetur sadipscing elitr, sed diam nonumy eirmod tempor invidunt ut labore et dolore</li>
    </ul>
  </div>
  <div class="footer"><span>13.11.16</span><span>FOOTER</span><span>10</span></div>
</section>

<section class="slide c2 r4">
  <div class="band-back"></div><div class="band"></div>
  <div class="headline" style="top:23px">Headline</div><div class="brand">PLAYNOVA</div>
  <div class="abs" style="left:19px;top:52px;font-size:7px;color:var(--ink-dark);font-weight:600;letter-spacing:1px">Title <span style="font-size:4.5px;font-weight:400">Text</span></div>
  <svg class="abs" style="left:18px;top:60px" width="180" height="64" viewBox="0 0 180 64" font-family="Open Sans, sans-serif" font-size="3.5" fill="#4a4a4a">
    <g stroke="#e3e3e3" stroke-width=".4"><line x1="12" y1="6" x2="154" y2="6"/><line x1="12" y1="18" x2="154" y2="18"/><line x1="12" y1="30" x2="154" y2="30"/><line x1="12" y1="42" x2="154" y2="42"/><line x1="12" y1="54" x2="154" y2="54"/></g>
    <text x="3" y="7">80</text><text x="3" y="19">60</text><text x="3" y="31">40</text><text x="3" y="43">20</text><text x="5" y="55">0</text>
    <polyline fill="none" stroke="#3aa8ea" stroke-width="1" points="16,43 26,38 36,20 46,15 56,19 66,22 76,21 86,22 96,24 106,23 116,31 126,26 136,25"/>
    <polyline fill="none" stroke="#8fbc2a" stroke-width="1" points="16,46 26,41 36,23 46,17 56,21 66,24 76,23 86,24 96,26 106,25 116,33 126,28 136,27"/>
    <line x1="148" y1="46" x2="154" y2="46" stroke="#8fbc2a"/><text x="155" y="47.5">Text</text>
    <line x1="148" y1="52" x2="154" y2="52" stroke="#3aa8ea"/><text x="155" y="53.5">Text</text>
    <g text-anchor="middle"><text x="16" y="61">Text</text><text x="26" y="61">Text</text><text x="36" y="61">Text</text><text x="46" y="61">Text</text><text x="56" y="61">Text</text><text x="66" y="61">Text</text><text x="76" y="61">Text</text><text x="86" y="61">Text</text><text x="96" y="61">Text</text><text x="106" y="61">Text</text><text x="116" y="61">Text</text><text x="126" y="61">Text</text><text x="136" y="61">Text</text></g>
  </svg>
  <div class="abs" style="left:19px;top:128px;font-size:7px;color:var(--ink-dark);font-weight:600;letter-spacing:1px">Title <span style="font-size:4.5px;font-weight:400">Text</span></div>
  <svg class="abs" style="left:18px;top:136px" width="180" height="62" viewBox="0 0 180 62" font-family="Open Sans, sans-serif" font-size="3.5" fill="#4a4a4a">
    <g stroke="#e3e3e3" stroke-width=".4"><line x1="12" y1="5" x2="154" y2="5"/><line x1="12" y1="16" x2="154" y2="16"/><line x1="12" y1="27" x2="154" y2="27"/><line x1="12" y1="38" x2="154" y2="38"/><line x1="12" y1="49" x2="154" y2="49"/></g>
    <text x="3" y="6">40</text><text x="3" y="17">30</text><text x="3" y="28">20</text><text x="3" y="39">10</text><text x="5" y="50">0</text>
    <g fill="#8fbc2a"><rect x="14" y="26" width="3" height="23"/><rect x="24" y="24" width="3" height="25"/><rect x="34" y="20" width="3" height="29"/><rect x="44" y="27" width="3" height="22"/><rect x="54" y="28" width="3" height="21"/><rect x="64" y="29" width="3" height="20"/><rect x="74" y="26" width="3" height="23"/><rect x="84" y="29" width="3" height="20"/><rect x="94" y="27" width="3" height="22"/><rect x="104" y="29" width="3" height="20"/><rect x="114" y="26" width="3" height="23"/><rect x="124" y="28" width="3" height="21"/><rect x="134" y="30" width="3" height="19"/></g>
    <g fill="#3aa8ea"><rect x="18" y="24" width="3" height="25"/><rect x="28" y="22" width="3" height="27"/><rect x="38" y="18" width="3" height="31"/><rect x="48" y="25" width="3" height="24"/><rect x="58" y="26" width="3" height="23"/><rect x="68" y="27" width="3" height="22"/><rect x="78" y="24" width="3" height="25"/><rect x="88" y="27" width="3" height="22"/><rect x="98" y="25" width="3" height="24"/><rect x="108" y="27" width="3" height="22"/><rect x="118" y="24" width="3" height="25"/><rect x="128" y="26" width="3" height="23"/><rect x="138" y="28" width="3" height="21"/></g>
    <rect x="148" y="42" width="2.5" height="2.5" fill="#3aa8ea"/><text x="152" y="44.5">Text</text>
    <rect x="148" y="48" width="2.5" height="2.5" fill="#8fbc2a"/><text x="152" y="50.5">Text</text>
    <g text-anchor="middle"><text x="18" y="57">Text</text><text x="28" y="57">Text</text><text x="38" y="57">Text</text><text x="48" y="57">Text</text><text x="58" y="57">Text</text><text x="68" y="57">Text</text><text x="78" y="57">Text</text><text x="88" y="57">Text</text><text x="98" y="57">Text</text><text x="108" y="57">Text</text><text x="118" y="57">Text</text><text x="128" y="57">Text</text><text x="138" y="57">Text</text></g>
  </svg>
  <div class="card-back" style="left:223px;top:60px;width:132px;height:130px"></div>
  <div class="card" style="left:219px;top:62px;width:128px;height:122px">
    <ul class="bullets">
      <li>Lorem ipsum dolor sit amet, consetetur sadipscing elitr, sed diam nonumy eirmod tempor invidunt ut labore et dolore</li>
      <li>Lorem ipsum dolor sit amet, consetetur sadipscing elitr, sed diam nonumy eirmod tempor invidunt ut labore et dolore</li>
    </ul>
  </div>
  <div class="footer"><span>13.11.16</span><span>FOOTER</span><span>11</span></div>
</section>

<section class="slide c3 r4">
  <div class="band-back"></div><div class="band"></div>
  <div class="headline" style="top:23px">Headline</div><div class="brand">PLAYNOVA</div>
  <table class="data">
    <tr><td>Text</td><td>Text</td><td>Text</td><td>Text</td><td>Text</td></tr>
    <tr><td>Text</td><td>11</td><td>12</td><td>13</td><td>14</td></tr>
    <tr><td>Text</td><td>56</td><td>60</td><td>64</td><td>68</td></tr>
    <tr><td>Text</td><td>21</td><td>22</td><td>23</td><td>24</td></tr>
    <tr><td>Text</td><td>14</td><td>14</td><td>15</td><td>16</td></tr>
    <tr><td>Text</td><td>4</td><td>4</td><td>4</td><td>4</td></tr>
    <tr><td>Text</td><td>106</td><td>112</td><td>119</td><td>126</td></tr>
  </table>
  <div class="card-back" style="left:222px;top:60px;width:132px;height:130px"></div>
  <div class="card" style="left:218px;top:62px;width:128px;height:122px">
    <ul class="bullets">
      <li>Lorem ipsum dolor sit amet, consetetur sadipscing elitr, sed diam nonumy eirmod tempor invidunt ut labore et dolore</li>
      <li>Lorem ipsum dolor sit amet, consetetur sadipscing elitr, sed diam nonumy eirmod tempor invidunt ut labore et dolore</li>
    </ul>
  </div>
  <div class="footer"><span>13.11.16</span><span>FOOTER</span><span>12</span></div>
</section>

</body>
</html>
```